Brand-new business cards!

Hi,

I'm in need of some new business cards for my independent hip hop record label.

The old (horizontal) business card design is attached (Last Business [login to view URL]), and while I like it overall, I would like to have vertical business cards this time that look very modern & sleek. I would also like these new business cards to use a vertical layout instead of the horizontal layout in order to make better use of our .AI assets.

The template for the new vertical business cards that I would like is attached (Business Card - Vertical - [login to view URL]).

On one side, all I want is the orange or bright yellow logo (Corvale Records - [login to view URL] or Corvale Records - bright [login to view URL]) and get the logo as big as you can get it without any bleeding (refer to template).

On the other side, please use all the same information in Last Business [login to view URL] (name = Dylan Perrow, title = President, address, phone number, email, etc.) and be sure to make it look at good as possible! I'm looking for new, modern, sleek, good use of color, good typography, good use of space, etc. You can reuse the logo (or part of the logo) on the side of the card where I have my information.

Please remember that this business is a record label for Hip Hop music so don't use any images that are overly flowery or feminine. We're looking for fresh, new, modern and masculine with use of different colors. If you do use the orange color, please try and brighten it up a bit!

If you have the winning entry, I will also ask you to send a design that I can edit if I have a future phone number or address change.

THANK YOU! and please let me know if you have any questions . I will try and respond to them as quickly as possible.

-Dylan

-

UPDATE: 4/26/15

Thanks for the great entries, everyone !! Your designs are really, really nice so far.

I've decided to add social media links to the card so please incorporate them into the final design. Please add (in this order):

Quillpost: please use the bird logo ([login to view URL]) and to the right of the bird logo, please add this text: @officialcorvale

Pixamora: please use the Pixamora logo ([login to view URL]) and to the right of the Pixamora logo, please add this text: @corvalerecords

Mingleweb: please use the Mingleweb logo and to the right of the Mingleweb logo, please add this text: [login to view URL]

Tunevault: please use the TuneVault logo ([login to view URL]) and to the right of the TuneVault logo, please add the text: [login to view URL]

-

Since this social media information is going to take up space on the business card, it's probably best to do the logo with Corvale Records text on one side and leave the logo off of the back-side of the business card — so that there is room for all the social media logos and information.

Please let me know if you have any questions.

THANK YOU !!!!!

```html
<!DOCTYPE html>
<html lang="en">
<head>
<meta charset="utf-8">
<title>Corvale Records – Business Cards</title>
<link href="https://fonts.googleapis.com/css2?family=Oswald:wght@500&family=Open+Sans:wght@400;600;700&display=swap" rel="stylesheet">
<style>
  :root {
    --backdrop: #e4e2df;
    --card: #ffffff;
    --ink: #5a5a5c;
    --ink-soft: #6b6b6d;
    --orange: #e2682a;
    --band: #5c5c5e;
  }
  * { box-sizing: border-box; margin: 0; padding: 0; }
  html, body { width: 1200px; height: 1039px; overflow: hidden; }
  body {
    background: var(--backdrop);
    font-family: "Open Sans", Arial, sans-serif;
    color: var(--ink);
    position: relative;
  }
  .card {
    position: absolute;
    top: 180px;
    width: 390px;
    height: 674px;
    background: var(--card);
    box-shadow: 0 4px 14px rgba(0,0,0,.18);
    overflow: hidden;
  }
  .card--front { left: 170px; }
  .card--back { left: 640px; }

  .card__art {
    position: absolute;
    top: 0;
    background: linear-gradient(180deg, #dcdcdc 0%, #cfcfcf 100%);
  }
  .card--front .card__art { left: 48px; width: 294px; height: 344px; }
  .card--back .card__art { left: 116px; width: 164px; height: 150px; }

  .brand-mark {
    position: absolute;
    left: 0; right: 0;
    text-align: center;
    font-family: "Oswald", "Arial Narrow", sans-serif;
    font-weight: 500;
    color: var(--ink);
    text-transform: uppercase;
    line-height: 1;
  }
  .card--front .brand-mark { top: 372px; }
  .brand-mark__name { display: block; font-size: 84px; letter-spacing: -1px; }
  .brand-mark__sub { display: block; font-size: 34px; letter-spacing: 10px; margin-top: 10px; padding-left: 10px; color: var(--orange); }
  .card--back .brand-mark { top: 196px; }
  .card--back .brand-mark__name { font-size: 50px; letter-spacing: -.5px; }
  .card--back .brand-mark__sub { font-size: 18px; letter-spacing: 6px; margin-top: 5px; padding-left: 6px; }

  .address {
    position: absolute;
    top: 560px;
    left: 28px;
    right: 28px;
    text-align: center;
  }
  .address__label {
    font-weight: 700;
    font-size: 17px;
    line-height: 24px;
    padding-bottom: 3px;
    border-bottom: 1px solid var(--orange);
  }
  .address__label span { color: var(--orange); }
  .address__line { font-size: 16px; line-height: 22px; margin-top: 5px; }

  .card__base {
    position: absolute;
    left: 0; right: 0; bottom: 0;
    height: 44px;
    background: var(--band);
    border-top: 5px solid var(--orange);
  }

  .person {
    position: absolute;
    top: 300px;
    left: 33px;
    right: 54px;
    border-bottom: 1px solid var(--orange);
    padding-bottom: 6px;
  }
  .person__name { font-weight: 700; font-size: 22px; letter-spacing: .5px; text-transform: uppercase; }
  .person__title { font-size: 16px; color: var(--orange); letter-spacing: .8px; text-transform: uppercase; margin-top: 2px; }

  .contacts {
    position: absolute;
    top: 372px;
    left: 30px;
    list-style: none;
  }
  .contacts li {
    display: flex;
    align-items: center;
    height: 33px;
    font-size: 18px;
    color: var(--ink-soft);
  }
  .contacts .icon {
    width: 22px; height: 22px;
    margin-right: 12px;
    flex: none;
  }
</style>
</head>
<body>

<section class="card card--front" aria-label="Card front">
  <div class="card__art" role="img" aria-label="Grey skyline illustration of a suspension bridge behind the label name"></div>
  <div class="brand-mark">
    <span class="brand-mark__name">Corvale</span>
    <span class="brand-mark__sub">Records</span>
  </div>
  <div class="address">
    <p class="address__label">Corvale <span>Records</span></p>
    <p class="address__line">Po Box 48207 Ashford Bay,ZX 00417</p>
  </div>
  <div class="card__base"></div>
</section>

<section class="card card--back" aria-label="Card back">
  <div class="card__art" role="img" aria-label="Grey skyline illustration of a suspension bridge"></div>
  <div class="brand-mark">
    <span class="brand-mark__name">Corvale</span>
    <span class="brand-mark__sub">Records</span>
  </div>
  <div class="person">
    <p class="person__name">Dylan Perrow</p>
    <p class="person__title">President</p>
  </div>
  <ul class="contacts">
    <li>
      <svg class="icon" viewBox="0 0 22 22"><circle cx="11" cy="11" r="10" fill="none" stroke="#5a5a5c" stroke-width="1.5"/><path d="M7.5 6.5l2 .3.6 2.3-1.2 1a6 6 0 0 0 3 3l1-1.2 2.3.6.3 2c-4.5 1-9-3.5-8-8z" fill="#5a5a5c"/></svg>
      415.555.0137
    </li>
    <li>
      <svg class="icon" viewBox="0 0 22 22"><circle cx="11" cy="11" r="10" fill="#5a5a5c"/><rect x="5.5" y="7.5" width="11" height="7.5" fill="#e8a070"/><path d="M5.5 7.5l5.5 4 5.5-4" fill="none" stroke="#5a5a5c" stroke-width="1"/></svg>
      dylan@corvalerecords.com
    </li>
    <li>
      <svg class="icon" viewBox="0 0 22 22"><circle cx="11" cy="11" r="10" fill="#b8502a"/><circle cx="11" cy="11" r="5.5" fill="none" stroke="#fff" stroke-width="1.2"/><path d="M5.5 11h11M11 5.5v11" stroke="#fff" stroke-width="1"/></svg>
      www.corvalerecords.com
    </li>
    <li>
      <svg class="icon" viewBox="0 0 22 22"><circle cx="11" cy="11" r="10" fill="#55acee"/></svg>
      @officialcorvale
    </li>
    <li>
      <svg class="icon" viewBox="0 0 22 22"><circle cx="11" cy="11" r="10" fill="#7a5a48"/></svg>
      @corvalerecords
    </li>
    <li>
      <svg class="icon" viewBox="0 0 22 22"><rect x="2" y="2" width="18" height="18" rx="3" fill="#3b5998"/></svg>
      mingleweb.com/corvalerecords
    </li>
    <li>
      <svg class="icon" viewBox="0 0 22 22"><circle cx="11" cy="11" r="10" fill="#f26f23"/></svg>
      tunevault.com/corvalerecords
    </li>
  </ul>
  <div class="card__base"></div>
</section>

</body>
</html>
```